stationery
business cards, letterhead, and envelopes
Professional
Marisol Dunkerly
Mortgage Loan Originator / Owner
418 Kettering Avenue Ste 2270
Honolulu HI 96813
TideRiverCredit@quillmail.com
www.BrightCedarLending.com
Lowest Rates In Hawaii !!!!!

```html
<!DOCTYPE html>
<html lang="en">
<head>
<meta charset="utf-8">
<title>Bright Cedar Lending — Stationery</title>
<link href="https://fonts.googleapis.com/css2?family=Montserrat:wght@400;600;700&display=swap" rel="stylesheet">
<style>
  :root{
    --stage:#ecebe8;
    --paper:#ffffff;
    --blue:#2f44a0;
    --navy:#1e2c78;
    --grey:#7d7f86;
    --grey-light:#c9cacd;
    --sand:#efe6d4;
    --ink:#3a3f55;
  }
  *{box-sizing:border-box;margin:0;padding:0}
  html,body{width:1200px;height:598px;overflow:hidden}
  body{background:var(--stage);font-family:'Montserrat',sans-serif;color:var(--ink);position:relative}
  .sheet{position:absolute;background:var(--paper);box-shadow:0 2px 6px rgba(0,0,0,.18);overflow:hidden}
  .brand{display:flex;align-items:center;gap:6px;color:var(--blue);font-weight:700;white-space:nowrap}
  .brand-dot{border-radius:50%;background:var(--blue);flex:none}
  .tagline{color:var(--grey);font-size:6px;letter-spacing:.5px;text-transform:uppercase;white-space:nowrap}
  .emblem{position:absolute;border-radius:50%;background:radial-gradient(circle,#f3ecdd 0%,#eadfc7 70%,#e6dcc8 100%);opacity:.6}
  .wave{position:absolute;left:0;width:100%}
  .caption{position:absolute;top:566px;font-size:9px;letter-spacing:2px;text-transform:uppercase;color:#555}

  /* business cards */
  .card{left:24px;width:180px;height:106px}
  .card-front{top:235px}
  .card-back{top:370px}
  .card .brand{position:absolute;left:0;width:100%;justify-content:center}
  .card .tagline{position:absolute;left:0;width:100%;text-align:center;font-size:4.5px}
  .card-front .brand{top:12px;font-size:9px;gap:5px}
  .card-front .brand-dot{width:7px;height:7px}
  .card-front .tagline{top:26px}
  .card-contact{position:absolute;left:9px;top:70px;width:84px;color:#fff;font-size:4.2px;line-height:6.6px;white-space:nowrap}
  .card-name{position:absolute;right:9px;top:71px;width:76px;color:#fff;text-align:right;font-size:3.7px;line-height:6px;white-space:nowrap}
  .card-name b{font-size:6.5px;font-weight:600;display:block;line-height:9px}
  .card-back .brand{top:38px;font-size:10px}
  .card-back .brand-dot{width:8px;height:8px}
  .card-back .tagline{top:54px}

  /* letterhead */
  .letterhead{left:218px;top:26px;width:370px;height:512px}
  .letterhead .brand{position:absolute;left:22px;top:22px;font-size:17px}
  .letterhead .brand-dot{width:14px;height:14px}
  .letterhead .tagline{position:absolute;left:22px;top:46px}
  .letterhead .emblem{left:120px;top:170px;width:130px;height:130px}
  .lh-contact{position:absolute;left:20px;bottom:14px;color:#fff;font-size:5.5px;line-height:9px}
  .lh-contact .row{display:flex;align-items:center;gap:5px}
  .icon{width:6px;height:6px;flex:none}

  /* envelopes */
  .envelope{left:720px;width:430px}
  .env-blue{top:24px;height:150px}
  .env-grey{top:132px;height:134px}
  .env-back{top:240px;height:160px}
  .env-front{top:355px;height:192px}
  .env-flap{position:absolute;left:0;top:0;width:100%}
  .env-back .seal{position:absolute;left:202px;top:124px;width:26px;height:26px;border-radius:50%;background:var(--blue)}
  .env-front .brand{position:absolute;left:24px;top:22px;font-size:17px}
  .env-front .brand-dot{width:14px;height:14px}
  .env-front .tagline{position:absolute;left:24px;top:46px}
  .env-front .emblem{left:262px;top:78px;width:100px;height:100px}
</style>
</head>
<body>

<!-- business card front -->
<section class="sheet card card-front">
  <div class="brand"><span class="brand-dot"></span>Bright Cedar Lending</div>
  <p class="tagline">Lowest Rates In Hawaii !!!!!</p>
  <svg class="wave" style="top:44px;height:62px" viewBox="0 0 180 62" preserveAspectRatio="none">
    <path d="M0 14 C60 -4 120 30 180 8 L180 62 L0 62 Z" fill="var(--grey-light)"/>
    <path d="M0 20 C60 4 120 36 180 14 L180 62 L0 62 Z" fill="var(--blue)"/>
  </svg>
  <div class="card-contact">
    (808) 555-0142<br>TideRiverCredit@quillmail.com<br>www.BrightCedarLending.com<br>418 Kettering Avenue Ste 2270
  </div>
  <div class="card-name"><b>Marisol Dunkerly</b>Mortgage Loan Originator / Owner</div>
</section>

<!-- business card back -->
<section class="sheet card card-back">
  <div class="brand"><span class="brand-dot"></span>Bright Cedar Lending</div>
  <p class="tagline">Lowest Rates In Hawaii !!!!!</p>
</section>

<!-- letterhead -->
<section class="sheet letterhead">
  <div class="brand"><span class="brand-dot"></span>Bright Cedar Lending</div>
  <p class="tagline">Lowest Rates In Hawaii !!!!!</p>
  <div class="emblem" role="img" aria-label="Faint palm tree emblem watermark"></div>
  <svg class="wave" style="bottom:0;height:100px" viewBox="0 0 370 100" preserveAspectRatio="none">
    <path d="M0 18 C120 70 250 -10 370 30 L370 100 L0 100 Z" fill="var(--grey-light)"/>
    <path d="M0 30 C120 78 250 4 370 40 L370 100 L0 100 Z" fill="var(--blue)"/>
    <path d="M0 24 C120 74 250 -4 370 34" fill="none" stroke="var(--grey)" stroke-width="1.5"/>
  </svg>
  <div class="lh-contact">
    <div class="row"><svg class="icon" viewBox="0 0 10 10"><path d="M2 1l2 2-1 1.5c.8 1.4 1.6 2.2 3 3L7.5 6l2 2-1.5 1.5C4 9 1 6 .5 2z" fill="#fff"/></svg>(808) 555-0142</div>
    <div class="row"><svg class="icon" viewBox="0 0 10 10"><path d="M2 1l2 2-1 1.5c.8 1.4 1.6 2.2 3 3L7.5 6l2 2-1.5 1.5C4 9 1 6 .5 2z" fill="#fff"/></svg>(808) 555-0187</div>
    <div class="row"><svg class="icon" viewBox="0 0 10 10"><rect x="1" y="2" width="8" height="6" fill="none" stroke="#fff"/><path d="M1 2l4 3 4-3" fill="none" stroke="#fff"/></svg>TideRiverCredit@quillmail.com</div>
    <div class="row"><svg class="icon" viewBox="0 0 10 10"><path d="M5 .5a3 3 0 0 1 3 3C8 6 5 9.5 5 9.5S2 6 2 3.5a3 3 0 0 1 3-3z" fill="#fff"/></svg>418 Kettering Avenue Ste 2270, Honolulu HI 96813</div>
  </div>
</section>
<p class="caption" style="left:340px">Letter Head Option 1</p>

<!-- envelope backs -->
<section class="sheet envelope env-blue">
  <svg class="env-flap" viewBox="0 0 430 70" style="height:70px" preserveAspectRatio="none">
    <path d="M0 0 H430 V40 Q420 60 395 62 H35 Q10 60 0 40 Z" fill="var(--blue)"/>
  </svg>
</section>
<section class="sheet envelope env-grey">
  <svg class="env-flap" viewBox="0 0 430 66" style="height:66px" preserveAspectRatio="none">
    <path d="M0 0 H430 V36 Q420 58 395 60 H35 Q10 58 0 36 Z" fill="var(--grey)"/>
  </svg>
</section>
<section class="sheet envelope env-back">
  <svg class="env-flap" viewBox="0 0 430 150" style="height:150px" preserveAspectRatio="none">
    <path d="M0 0 L215 140 L430 0" fill="none" stroke="#e1e2e5" stroke-width="2"/>
  </svg>
  <div class="seal" role="img" aria-label="Round palm tree seal"></div>
</section>

<!-- envelope front -->
<section class="sheet envelope env-front">
  <div class="brand"><span class="brand-dot"></span>Bright Cedar Lending</div>
  <p class="tagline">Lowest Rates In Hawaii !!!!!</p>
  <div class="emblem" role="img" aria-label="Faint palm tree emblem watermark"></div>
</section>
<p class="caption" style="left:862px">Envelope Option 2</p>

</body>
</html>
```